Lantern Hearthworks Business Cards

Looking to create simple business cards that highlight our unique three sided triangle fire pit design with the colors and font of our logo, listed below.

Colors

Designer to choose colors to be used in the design.

Requirements
Must have
• Looking for something simple that includes a picture of our fire pit with name, website (lanternhearthworks.com), phone number and email. Want to keep the color mostly orange and black.
• Font is gotham(medium) and orange color code is #ee6e22

```html
<!DOCTYPE html>
<html lang="en">
<head>
<meta charset="utf-8">
<title>Lantern Hearthworks Business Cards</title>
<link href="https://fonts.googleapis.com/css2?family=Montserrat:wght@400;500;700&display=swap" rel="stylesheet">
<style>
  :root {
    --stage: #2b2b2d;
    --card: #0e0e10;
    --orange: #ee6e22;
    --white: #f4f4f4;
    --fire-deep: #7a2a08;
    --fire-hot: #ffb347;
  }
  * { box-sizing: border-box; margin: 0; padding: 0; }
  html, body { width: 1200px; height: 878px; overflow: hidden; }
  body {
    background: var(--stage);
    font-family: "Montserrat", sans-serif;
    position: relative;
  }
  .card {
    position: absolute;
    left: 300px;
    width: 600px;
    height: 343px;
    background: var(--card);
    box-shadow: 0 14px 30px rgba(0,0,0,.55);
    overflow: hidden;
  }
  .card--front { top: 60px; }
  .card--back { top: 470px; }

  /* front */
  .firepit-photo { position: absolute; left: 150px; top: 52px; width: 240px; height: 230px; }
  .front-name {
    position: absolute; left: 410px; top: 150px;
    color: var(--orange); font-weight: 500;
    font-size: 17px; letter-spacing: 3px; text-transform: uppercase;
    line-height: 1.3; white-space: nowrap;
  }

  /* back */
  .brand {
    position: absolute; left: 56px; top: 62px;
    display: flex; align-items: center; gap: 16px;
  }
  .brand__dot { width: 22px; height: 22px; border-radius: 50%; background: var(--orange); }
  .brand__name {
    color: var(--orange); font-weight: 500;
    font-size: 24px; letter-spacing: 5px; text-transform: uppercase;
    white-space: nowrap;
  }
  .rule {
    position: absolute; left: 44px; top: 222px; width: 396px; height: 1px;
    background: var(--orange);
  }
  .person { position: absolute; right: 40px; top: 188px; text-align: right; }
  .person__name { color: var(--orange); font-weight: 700; font-size: 26px; line-height: 32px; }
  .person__role { color: var(--white); font-weight: 500; font-size: 14px; letter-spacing: .5px; margin-top: 6px; line-height: 18px; }
  .contacts { position: absolute; left: 40px; top: 248px; list-style: none; }
  .contacts li {
    display: flex; align-items: center; gap: 14px;
    color: var(--white); font-size: 16px; font-weight: 400; letter-spacing: .4px;
    height: 27px; white-space: nowrap;
  }
  .contacts svg { width: 16px; height: 16px; flex: none; }
  .contacts .accent { color: var(--orange); }
</style>
</head>
<body>
  <section class="card card--front">
    <svg class="firepit-photo" viewBox="0 0 240 230" role="img" aria-label="Photo of the three-sided triangle fire pit with burning logs and flames">
      <defs>
        <radialGradient id="fireGlow" cx="50%" cy="55%" r="60%">
          <stop offset="0" stop-color="var(--fire-hot)"/>
          <stop offset=".45" stop-color="var(--orange)"/>
          <stop offset="1" stop-color="var(--fire-deep)"/>
        </radialGradient>
      </defs>
      <polygon points="130,10 235,225 5,150" fill="url(#fireGlow)"/>
    </svg>
    <div class="front-name">Lantern<br>Hearthworks</div>
  </section>

  <section class="card card--back">
    <div class="brand">
      <span class="brand__dot"></span>
      <span class="brand__name">Lantern Hearthworks</span>
    </div>
    <div class="rule"></div>
    <div class="person">
      <div class="person__name">Owen Calder</div>
      <div class="person__role">Founder &amp; CEO</div>
    </div>
    <ul class="contacts">
      <li>
        <svg viewBox="0 0 16 16"><path d="M4 1.5l2.5 3-1.6 1.6a9 9 0 0 0 5 5l1.6-1.6 3 2.5-1.8 2.3C7 14 2 9 1.7 3.3z" fill="var(--orange)"/></svg>
        555 214 7730
      </li>
      <li>
        <svg viewBox="0 0 16 16"><rect x="1" y="3" width="14" height="10" fill="var(--orange)"/><path d="M1 3l7 6 7-6" fill="none" stroke="var(--card)" stroke-width="1.3"/></svg>
        hello@lanternhearthworks.com
      </li>
      <li>
        <svg viewBox="0 0 16 16"><circle cx="8" cy="8" r="6.5" fill="none" stroke="var(--orange)" stroke-width="1.4"/><path d="M1.5 8h13M8 1.5c-3 3-3 10 0 13M8 1.5c3 3 3 10 0 13" fill="none" stroke="var(--orange)" stroke-width="1.1"/></svg>
        <span>www.<span class="accent">lanternhearthworks</span>.com</span>
      </li>
    </ul>
  </section>
</body>
</html>
```